Design a label for a new brand of Gin the UK called Silver Tabby - featuring a cat

The gin is Persian Blue in Colour and owners of Persian Blue cats will be a target market - the bottle is very distinctive and lends itself to a square label.

The Marshmallow root used in the production will be a draw to customers. The bottle is flat with a large front face that lends itself to a striking design. There should be enough space around the label to show the blue gin in the bottle as this is a feature.

Target Market(s)

gin lovers who may also own a persian blue car - age group 30 - 60 primarily female

Font styles to use
Sans Serif
Script

Colors

Designer to choose colors to be used in the design.

Requirements
Must have
• The gin will be a persian blue colour so the label must standout or completment the gin in the bottle. Here is the bottle you are working with
• https://www.flaskmart-supply.co.uk/Glass-flasks/700ml-clear-glass-flask-Kellino.html
• Must have 70cl and 40% abv
Nice to have
• The predominent botanical (other than juniper) is marshmallow root, this is quite a sweet gin. The reference to marshmallow root would be a nice to have.

```html
<!DOCTYPE html>
<html lang="en">
<head>
<meta charset="utf-8">
<title>Silver Tabby Gin – Label</title>
<link href="https://fonts.googleapis.com/css2?family=Almendra+Display&family=Great+Vibes&family=Old+Standard+TT&display=swap" rel="stylesheet">
<style>
  :root {
    --paper: #ffffff;
    --label-rim: #5b5bd9;
    --label-deep: #2b2ba6;
    --label-mid: #6a6adf;
    --label-pale: #ffffff;
    --ink-light: #ffffff;
    --ink-accent: #5656cf;
    --art-tone: #8f8fe4;
    --art-tone-soft: #c9c9f2;
  }
  html, body {
    margin: 0;
    padding: 0;
    width: 1200px;
    height: 1000px;
    overflow: hidden;
    background: var(--paper);
  }
  .canvas {
    position: relative;
    width: 1200px;
    height: 1000px;
  }
  .gin-label {
    position: absolute;
    left: 270px;
    top: 142px;
    width: 660px;
    height: 716px;
  }
  .label-rim { fill: var(--label-rim); }
  .label-field { fill: url(#field-gradient); stroke: var(--ink-light); stroke-width: 3; }
  .brand-name {
    font-family: "Almendra Display", "Georgia", serif;
    fill: var(--ink-light);
    font-size: 84px;
  }
  .spirit-type {
    font-family: "Great Vibes", cursive;
    fill: var(--ink-accent);
    font-size: 18px;
  }
  .volume-strength {
    font-family: "Old Standard TT", "Times New Roman", serif;
    fill: var(--ink-accent);
    font-size: 10.5px;
    letter-spacing: 0.3px;
  }
  .rule-line { stroke: var(--ink-accent); stroke-width: 1.6; fill: none; }
  .flourish { fill: var(--ink-light); opacity: 0.35; }
  .flourish-small { fill: var(--ink-accent); opacity: 0.35; }
</style>
</head>
<body>
<main class="canvas">
  <svg class="gin-label" viewBox="0 0 422 458" xmlns="http://www.w3.org/2000/svg">
    <defs>
      <linearGradient id="field-gradient" x1="0" y1="0" x2="0" y2="1">
        <stop offset="0" stop-color="var(--label-deep)"/>
        <stop offset="0.45" stop-color="var(--label-mid)"/>
        <stop offset="0.9" stop-color="var(--label-pale)"/>
      </linearGradient>
      <linearGradient id="cat-gradient" x1="0" y1="0" x2="1" y2="1">
        <stop offset="0" stop-color="var(--art-tone)"/>
        <stop offset="1" stop-color="var(--art-tone-soft)"/>
      </linearGradient>
    </defs>

    <path class="label-rim" d="M0 82 L22 82 Q22 30 70 18 Q211 -8 352 18 Q400 30 400 82 L422 82 L422 392 L400 392 Q400 440 360 452 Q211 466 62 452 Q22 440 22 392 L0 392 Z"/>
    <path class="label-field" d="M28 92 L40 92 Q40 42 80 32 Q211 10 342 32 Q382 42 382 92 L394 92 L394 382 L382 382 Q382 428 348 438 Q211 454 74 438 Q40 428 40 382 L28 382 Z"/>

    <rect class="flourish" x="48" y="96" width="30" height="28" rx="12" role="img" aria-label="Scroll flourish ornament"/>
    <rect class="flourish" x="344" y="96" width="30" height="28" rx="12" role="img" aria-label="Scroll flourish ornament"/>

    <text class="brand-name" x="211" y="160" text-anchor="middle">Silver</text>
    <text class="brand-name" x="211" y="262" text-anchor="middle">Tabby</text>

    <text class="spirit-type" x="145" y="294" text-anchor="middle">Gin</text>

    <line class="rule-line" x1="64" y1="366" x2="352" y2="366"/>
    <rect class="flourish-small" x="50" y="356" width="14" height="14" rx="6" role="img" aria-label="Small curl ornament"/>
    <rect class="flourish-small" x="352" y="356" width="14" height="14" rx="6" role="img" aria-label="Small curl ornament"/>

    <rect x="107" y="300" width="190" height="132" rx="30" fill="url(#cat-gradient)" role="img" aria-label="Illustration of a long-haired cat lying down, tinted in soft blue"/>

    <text class="volume-strength" x="222" y="414" text-anchor="middle">70CL AND 40% ABV</text>
  </svg>
</main>
</body>
</html>
```